Wine Label Design

A wine label for 750ml bottles. Same label for different varieties with the variety / region / vintage to be updated as required.
Brand: Beyond the Ridge
Product Use: Front and Back label suitable for a 750 ml bottle (preferably Burgundy bottles)
Design Brief: Beyond the Ridge is a small winery that produces limited amounts of hand crafted wines that are aimed at the mid to top end of the market and requires a label befitting the work that goes into the creation of the wine. In terms of style i don't have any preconceptions and am open to a broad range of design suggestions at the same level of existing premium brands or innovative brands.
Must Have for Front label
Front Label
Beyond the Ridge
2013
Grampians
Shiraz
750ML (should be in smaller text)
Alc. 14% by Vol. (should be in smaller text)
Must Have for Back Label
Beyond the Ridge
2013
Grampians
Shiraz
www.beyondtheridge.com.au (should be in smaller text)
Product of Australia
Alc.14% by Vol. (should be in smaller text)
Contains preservative 220(should be in smaller text)
Below are some guides for dimensions:
The Front Label Size can be between
100 - 120 mm (Width) x 70 - 85 mm (Height)
The back label size can be between
90 mm (Width) x 70 - 85 mm (Height)
Target Market(s)
Medium to top end of the wine market who require the label to be a reflection of the wine.
Industry/Entity Type
Product
Colors
Designer to choose colors to be used in the design.
Look and feel

```html
<!DOCTYPE html>
<html lang="en">
<head>
<meta charset="utf-8">
<title>Beyond the Ridge – Wine Labels</title>
<link rel="stylesheet" href="https://fonts.googleapis.com/css2?family=Great+Vibes&family=Arimo:wght@400;700&display=swap">
<style>
  :root {
    --ink: #111111;
    --frame: #0b0b0b;
    --teal: #5fe0b6;
    --teal-deep: #3fcf9f;
    --teal-pale: #a9f0d6;
    --stage-dark: #b9bebe;
    --stage-light: #ffffff;
    --script: "Great Vibes", cursive;
    --sans: "Arimo", Arial, sans-serif;
  }
  * { box-sizing: border-box; margin: 0; padding: 0; }
  html, body { width: 1200px; height: 1200px; overflow: hidden; }
  body {
    position: relative;
    background: linear-gradient(100deg, var(--stage-dark) 0%, #dfe2e2 45%, var(--stage-light) 100%);
    font-family: var(--sans);
    color: var(--ink);
  }
  .label { position: absolute; background: var(--frame); }
  .label--front { left: 39px; top: 39px; width: 852px; height: 600px; padding: 25px 24px 24px 25px; }
  .label--back { left: 540px; top: 585px; width: 638px; height: 593px; padding: 15px 14px 14px 14px; }
  .label__face { position: relative; width: 100%; height: 100%; overflow: hidden; }
  .label__wash {
    position: absolute;
    inset: 0;
    background:
      radial-gradient(ellipse 30% 16% at 15% 96%, rgba(255,255,255,0.95), rgba(255,255,255,0) 100%),
      radial-gradient(ellipse 34% 18% at 55% 98%, rgba(255,255,255,0.9), rgba(255,255,255,0) 100%),
      radial-gradient(ellipse 26% 14% at 88% 95%, rgba(255,255,255,0.85), rgba(255,255,255,0) 100%),
      radial-gradient(ellipse 50% 20% at 50% 0%, rgba(200,250,230,0.55), rgba(255,255,255,0) 100%),
      linear-gradient(180deg, var(--teal-pale) 0%, var(--teal) 22%, var(--teal-deep) 55%, var(--teal) 75%, #d8f7ec 100%);
  }
  .label--back .label__wash {
    background:
      radial-gradient(ellipse 40% 14% at 20% 6%, rgba(255,255,255,0.85), rgba(255,255,255,0) 100%),
      radial-gradient(ellipse 30% 12% at 85% 4%, rgba(255,255,255,0.8), rgba(255,255,255,0) 100%),
      radial-gradient(ellipse 40% 10% at 50% 99%, rgba(255,255,255,0.85), rgba(255,255,255,0) 100%),
      linear-gradient(180deg, #c9f5e5 0%, var(--teal) 18%, var(--teal-deep) 55%, var(--teal) 85%, #c6f3e2 100%);
  }
  .label__text { position: absolute; white-space: nowrap; }
  .brand { font-family: var(--script); font-weight: 400; line-height: 1; transform-origin: center; }
  .label--front .brand { left: 0; width: 100%; top: 150px; text-align: center; font-size: 116px; transform: rotate(-4deg); }
  .label--back .brand { left: 0; width: 100%; top: 145px; text-align: center; font-size: 78px; transform: rotate(-4deg); }
  .vintage { font-weight: 700; letter-spacing: 1px; }
  .region { font-weight: 400; }
  .variety { font-weight: 700; letter-spacing: 0.5px; }
  .small { font-weight: 400; }
  .centered { left: 0; width: 100%; text-align: center; }

  .label--front .vintage { top: 292px; font-size: 23px; left: 27px; }
  .label--front .region { top: 345px; font-size: 17px; left: 27px; }
  .label--front .variety { top: 365px; font-size: 21px; left: 27px; }
  .label--front .volume { left: 25px; top: 491px; font-size: 15px; }
  .label--front .strength { right: 45px; top: 491px; font-size: 15px; }

  .label--back .vintage { top: 214px; font-size: 19px; left: -10px; }
  .label--back .region { top: 256px; font-size: 15px; left: -10px; }
  .label--back .variety { top: 274px; font-size: 18px; left: -10px; }
  .label--back .volume { top: 312px; font-size: 15px; left: -10px; }
  .label--back .strength { top: 430px; font-size: 15px; left: -8px; }
  .label--back .preservative { top: 464px; font-size: 14px; left: -8px; }
  .label--back .website { left: 53px; top: 500px; font-size: 15px; font-weight: 700; }
  .label--back .origin { right: 57px; top: 500px; font-size: 14px; }
</style>
</head>
<body>
  <section class="label label--front" aria-label="Front label">
    <div class="label__face">
      <div class="label__wash" role="img" aria-label="Mint green watercolour wash with white splashes along the bottom"></div>
      <h1 class="label__text brand">Beyond the Ridge</h1>
      <p class="label__text vintage centered">2013</p>
      <p class="label__text region centered">Grampians</p>
      <p class="label__text variety centered">SHIRAZ</p>
      <p class="label__text small volume">750ML</p>
      <p class="label__text small strength">Alc. 14% by Vol.</p>
    </div>
  </section>

  <section class="label label--back" aria-label="Back label">
    <div class="label__face">
      <div class="label__wash" role="img" aria-label="Mint green watercolour wash with white splashes at top and bottom"></div>
      <h2 class="label__text brand">Beyond the Ridge</h2>
      <p class="label__text vintage centered">2013</p>
      <p class="label__text region centered">Grampians</p>
      <p class="label__text variety centered">SHIRAZ</p>
      <p class="label__text small volume centered">750ML</p>
      <p class="label__text small strength centered">Alc.14% by Vol.</p>
      <p class="label__text small preservative centered">Contains preservative</p>
      <p class="label__text website">www.beyondtheridge.com.au</p>
      <p class="label__text small origin">Product of Australia</p>
    </div>
  </section>
</body>
</html>
```